Store Front Window Design

We have a beautiful corner store front dental practice with no window signage. Crazy I know...that's why we need your help.

The final design will be done in all vinyl unless unless you suggest a different medium (meaning we are open to some design idea like using frosted glass, etc...).

The windows provide a lot of natural light so the design needs to keep a lot of natural light coming into the office. Keep in mind vinyl is not opaque so keep the signage aesthetically pleasing and a minimalist design to allow as much natural light in as possible. The design should follow the aesthetic from our logo. or tie into at least. We want a cohesive brand aesthetic.

I submitted some general layout ideas. There is a blue banner with advertising words which we want to be used in the final version. Even though the lettering is black, in reality the letters will be a white vinyl on the outside of the window. When you submit your work, be sure to add any special instructions (aka tell me the vision for the letters is white not black, maybe gold leaf, or forested glass...stuff like that). AND YOU DO NOT HAVE TO FOLLOW MY PATTERN! YOU ARE ARTISTS AND WE ARE LOOKING FOR AN ARTISTIC EYE CATCHING PRESENTATION OF THIS INFORMATION. MAKE IT FLASHY AND ADD SOME AESTHETIC FROM THE TOOTH LOGO.

The store front is 6 windows roughly 60'' x 36'' The smaller windows below are 27'' x 36''. Around the corner there are 3 windows. they are 60'' x 27'' lower windows are 27" x 27". We would like to keep the bottom windows clear and keep the signage on the top windows, however, we are flexible.

The front 6 windows need to have this information worked into the design.

Practice name: Venn and Obradovic Dental & Orthodontics.
Phone numbers: Maren Venn DDS: 555.218.7043
Piotr Obradovic DDS:555.731.0962

Expertise: Dr. Venn General Dentistry & Orthodontics
Dr. Obradovic Oral Surgery & Sedation

Address: 4819 Thistle Rd

A banner across the bottom of the top windows with some key advertisement words: "Clearvetta" "Braces" "Implants" "Whiting" "Call today" "Free Consultation" "Oral Surgery" "Sedation". We like the two color idea. Its up to you to decide on the color combo. I used a Dark and light blue, but maybe a Blue and grey would nice to tire in the logo colors?

I have made some mock ideas to get the ball rolling but you do not have to stick to these designs at all, just as long as all the required information is there. Be creative with the layouts, fonts, color scheme, (just remember these are going on windows not necessarily a white background), and graphics/artistic flare (refer to logo for layout inspiration and use the logo as an actual graphic). We are running a miltimillion dollar dental practice so we want these windows to be eye catching to pull in patients and look like a million dollar design. Also all 6 windows dont need ot be used. I am really looking for creative design marketing.

The corner 3 windows need the following information: name, expertise, phone number, banner.

Dr. Venn, General Dentistry & Orthodontics, 555.218.7043
Dr. Obradovic, Oral Surgery & Sedation, 555.731.0962

There is also a front door that needs to be designed. The door is 60'' x 36'' (standard door size) We want simple white vinyl on the outside of the door. We need you to organize the information on the door, pick a easy to read font, maybe use the logo and use some of the front window signage aesthetic? Its up to you...but we we were initially thinking of just making the litters white and keep it simple but again you are the designers.

Practice name: Venn and Obradovic General Dentistry & Orthodontics

Address: 4819 Thistle Rd

Phone numbers: Dr. Venn 555.218.7043
Dr. Obradovic 555.731.0962

Hours of operation: Mon: call for an appointment
Tues-Thurs: 9am-5pm
Sat: call for an appointment
Sun: Closed

A line saying we speak Spanish: Se Habla Espanol

*****************************************************************************************************
here are some design that we liked and some rough sketches I made to start the ball rolling. Keep in mind that there are 9 windows for the front because its a corner office, but not all of them have to have stuff on it. We want simple, streamline, classy high commanding price point aesthetic. I am hiring you for your artistic minds.

Target Market(s)

anyone who has dental needs

Industry/Entity Type

Dental

Font styles to use
Serif
Sans Serif

Colors

Designer to choose colors to be used in the design.

Requirements
Must have
• 1. The required information (see project description)
• 2. Logo
• 3. Advertisement banner running along the bottom of all 9 windows (6 in front and 3 on the side)
• NOTE: Look at pictures of the store to get a sense of the customers point of view and also as a reference to how your design will be broken up across several windows or maybe you design something special for every window. But we want the banner to run along all the windows to lead customs to the door on the side. Finally the letters will be done in white vinyl unless state otherwise, remember the window needs to let in natural light so the entire window can not be covered in vinyl.
Nice to have
• artistic flare yet simple and sleep and expensive looking aesthetic. work logo into the design.
Should not have
• The goal is to catch someone eye and give them important information about the practice.
• It should not just be words.
• It should not have to many words
• It must be readable font for cards driving by.

```html
<!DOCTYPE html>
<html lang="en">
<head>
<meta charset="utf-8">
<title>Venn and Obradovic Dental &amp; Orthodontics – Storefront Window Graphics</title>
<link rel="stylesheet" href="https://fonts.googleapis.com/css2?family=Montserrat:wght@500;600&family=Oswald:wght@300&family=Nunito+Sans:wght@400&display=swap">
<style>
  :root {
    --page: #e6e6e6;
    --grey: #8c8c8e;
    --grey-light: #bdbdbf;
    --grey-pale: #dcdcdd;
    --grey-text: #7a7a7c;
    --blue: #1479cc;
    --white: #ffffff;
  }
  * { margin: 0; padding: 0; box-sizing: border-box; }
  html, body { width: 1165px; height: 1200px; overflow: hidden; background: var(--page); }

  .window-graphic {
    position: absolute;
    left: 40px;
    top: 381px;
    width: 1343px;
    height: 541px;
    transform: scale(0.808);
    transform-origin: 0 0;
    box-shadow: 0 18px 28px rgba(0,0,0,0.18);
    overflow: hidden;
  }
  .window-graphic__shapes { position: absolute; inset: 0; width: 100%; height: 100%; }

  .brand-mark {
    position: absolute;
    left: 498px; top: 30px;
    width: 120px; height: 120px;
    border-radius: 50%;
    background: var(--grey-light);
  }

  .practice-name {
    position: absolute;
    left: 0; width: 1114px;
    top: 170px;
    text-align: center;
    font-family: "Montserrat", sans-serif;
    font-weight: 600;
    color: var(--blue);
    text-transform: uppercase;
  }
  .practice-name__top { display: block; font-size: 21px; letter-spacing: 0.42em; line-height: 30px; }
  .practice-name__bottom { display: block; font-size: 29px; letter-spacing: 0.01em; line-height: 32px; }

  .info-row { position: absolute; top: 266px; left: 0; width: 1120px; height: 110px; }
  .info-cell {
    position: absolute; width: 240px; margin-left: -120px; text-align: center;
  }
  .doctor, .address-line {
    font-family: "Oswald", sans-serif;
    font-weight: 300;
    color: var(--blue);
    font-size: 38px;
    line-height: 45px;
    text-transform: uppercase;
  }
  .specialty, .address-label {
    font-family: "Nunito Sans", sans-serif;
    color: var(--grey-text);
    font-size: 22px;
    line-height: 28px;
  }
  .address-label { margin-top: 2px; }

  .service-banner { position: absolute; top: 375px; left: 0; width: 1135px; height: 40px; }
  .service-label {
    position: absolute; top: 11px; width: 200px; margin-left: -100px; text-align: center;
    font-family: "Montserrat", sans-serif; font-weight: 500;
    color: var(--white); font-size: 15px; text-transform: uppercase;
  }

  .service-icon {
    position: absolute; top: 456px; width: 96px; height: 46px; margin-left: -48px;
    background: var(--blue); border-radius: 8px;
  }

  .brand-decoration {
    position: absolute;
    left: 1150px; top: 30px;
    width: 193px; height: 480px;
    border-radius: 90px 0 0 90px;
    background: linear-gradient(180deg, var(--grey-pale), var(--grey-light));
  }
</style>
</head>
<body>
  <main class="window-graphic">
    <svg class="window-graphic__shapes" viewBox="0 0 1343 541" aria-hidden="true">
      <rect width="1343" height="541" fill="var(--grey)"/>
      <path d="M0,205 C70,80 180,12 330,0 L250,0 C130,20 45,95 0,185 Z" fill="var(--blue)"/>
      <path d="M0,235 C70,90 200,10 345,0 L1095,0 C1170,120 1180,330 1085,541 L0,541 Z" fill="var(--white)"/>
      <path d="M1150,180 C1200,320 1175,440 1140,541 L1085,541 C1160,400 1168,300 1150,180 Z" fill="var(--blue)"/>
      <rect x="0" y="375" width="1135" height="40" fill="var(--blue)"/>
      <line x1="0" y1="380" x2="1135" y2="380" stroke="var(--white)" stroke-width="1" stroke-dasharray="4 3"/>
      <line x1="0" y1="410" x2="1135" y2="410" stroke="var(--white)" stroke-width="1" stroke-dasharray="4 3"/>
    </svg>

    <div class="brand-decoration" role="img" aria-label="Large practice emblem decoration"></div>

    <div class="brand-mark" aria-hidden="true"></div>
    <h1 class="practice-name">
      <span class="practice-name__top">Venn and Obradovic</span>
      <span class="practice-name__bottom">Dental &amp; Orthodontics</span>
    </h1>

    <section class="info-row">
      <div class="info-cell" style="left:113px"><p class="doctor">Dr. Venn<br>555.218.7043</p></div>
      <div class="info-cell" style="left:336px;top:2px"><p class="specialty">General Dentistry<br>&amp;<br>Orthodontics</p></div>
      <div class="info-cell" style="left:557px"><p class="doctor">Dr. Obradovic<br>555.731.0962</p></div>
      <div class="info-cell" style="left:781px;top:2px"><p class="specialty">Oral Surgery &amp;<br>Sedationeral<br>Dentistry</p></div>
      <div class="info-cell" style="left:1010px"><p class="address-line">4819 Thistle Rd</p><p class="address-label">Address</p></div>
    </section>

    <nav class="service-banner">
      <span class="service-label" style="left:113px">Clearvetta</span>
      <span class="service-label" style="left:336px">Braces</span>
      <span class="service-label" style="left:557px">Implants</span>
      <span class="service-label" style="left:786px">Whiting</span>
      <span class="service-label" style="left:1010px">Oral Surgery</span>
    </nav>

    <div class="service-icon" style="left:113px" role="img" aria-label="Clear aligner tray icon"></div>
    <div class="service-icon" style="left:336px;width:66px;margin-left:-33px" role="img" aria-label="Teeth with braces icon"></div>
    <div class="service-icon" style="left:559px;width:34px;margin-left:-17px" role="img" aria-label="Dental implant icon"></div>
    <div class="service-icon" style="left:786px;width:46px;margin-left:-23px" role="img" aria-label="Sparkling white tooth icon"></div>
    <div class="service-icon" style="left:1012px;width:60px;margin-left:-30px" role="img" aria-label="Tooth with dental instruments icon"></div>
  </main>
</body>
</html>
```